Green Logistics / Last Mile Delivery Firm needs cool one-page website

FYI - We do have a detailed brief in the uploaded files section below
COMPANY
We recently launched the company Quillby Logistics which is a pioneer in urban green logistics and provides zero-emissions last mile delivery services (i.e. delivery of parcels with delivery vans to the doorstep of households) for its logistics and retail clients.
We take on urban parcel delivery for our clients with a 100% electric commercial vehicles fleet, fair and sustainable working conditions for our employees and an unparalleled professional and customer-focused mindset.
WEBSITE
In the detailed brief, we have provided examples to emulate. We need the design + coding of the website. Website needs to be friendly/optimized for and should open swiftly on both Android & iOS.
In general, the website should convey
- green mission of the company
- sustainability (good working conditions, focus on employees)
- customer orientation
- professionalism
DESIGN
In the detailed brief, we have provided designs to emulate.
Color design: we do have a logo which features 2 green colors (one lighter and one darker color tone). However, the colors on the website do not necessarily need to follow these 2 colors exactly as we are able to switch the logo colors.
Imagery: should reflect maybe 50% green/leaf/tree , 25% customer and employee orientation, and 25% logistics (here it's important that it is the last mile delivery, i.e. delivery with delivery vans to the doorstep of households)

```html
<!DOCTYPE html>
<html lang="en">
<head>
<meta charset="utf-8">
<title>Quillby Logistics – Sustainable Last Mile</title>
<link href="https://fonts.googleapis.com/css2?family=Montserrat:wght@600;700;800&family=Open+Sans:wght@400;600;700&display=swap" rel="stylesheet">
<style>
:root{
  --green:#3fa535;
  --green-dark:#1f7a2a;
  --green-deep:#145a1e;
  --lime:#8cc63f;
  --red:#e53935;
  --ink:#2b2b2b;
  --muted:#666;
  --light:#f4f7f2;
  --line:#e3e3e3;
  --dark:#1d1d1d;
}
*{box-sizing:border-box;margin:0;padding:0}
html,body{width:1200px;height:5060px;overflow:hidden}
body{font-family:"Open Sans",Arial,sans-serif;color:var(--ink);background:#fff;font-size:14px;line-height:1.6;position:relative}
h1,h2,h3,h4{font-family:"Montserrat",Arial,sans-serif}
.abs{position:absolute}
.eyebrow{font-size:11px;letter-spacing:2px;color:var(--green);text-transform:uppercase;text-align:center;font-weight:600}
.section-title{font-size:40px;text-align:center;color:var(--ink);font-weight:700;line-height:1.3}
.heart{display:block;margin:6px auto 0;width:22px;height:20px}
.btn{display:inline-flex;align-items:center;gap:10px;background:var(--lime);color:#fff;font-weight:700;font-size:13px;border-radius:30px;padding:12px 28px;text-transform:uppercase;font-family:"Montserrat",sans-serif}
.btn .dot{width:22px;height:22px;border-radius:50%;background:#fff}

/* top bar + nav */
.topbar{top:0;left:0;width:1200px;height:40px;background:#111;color:#ddd;font-size:12px;display:flex;align-items:center;gap:30px;padding-left:160px}
.topbar span{display:flex;align-items:center;gap:8px}
.nav{top:40px;left:0;width:1200px;height:80px;background:rgba(20,30,20,.85);display:flex;align-items:center;padding:0 160px}
.brand{display:flex;align-items:center;gap:10px;color:#fff;font-family:"Montserrat",sans-serif;font-weight:700;font-size:18px}
.brand i{width:26px;height:26px;border-radius:50%;background:var(--lime);display:block}
.menu{margin-left:auto;display:flex;gap:34px;font-family:"Montserrat",sans-serif;font-size:13px;font-weight:700;color:#fff}
.menu .active{color:var(--lime);border-bottom:2px solid var(--lime);padding-bottom:4px}
.lang{display:flex;gap:8px;margin-left:60px}
.lang span{width:26px;height:18px;background:#ccc;display:block}
.lang span+span{background:#e5b800}

/* hero */
.hero{top:0;left:0;width:1200px;height:820px;background:linear-gradient(120deg,#1a5a22 0%,#3a8d2f 45%,#6fae4a 75%,#2e6a2b 100%)}
.hero-content{top:395px;left:0;width:1200px;color:#fff;text-align:center}
.hero-content .eyebrow{color:#fff;margin-bottom:10px}
.hero-content h1{font-size:29px;font-weight:800;letter-spacing:.3px;white-space:nowrap}
.hero-content p{width:760px;margin:18px auto 28px;font-size:14.5px}
.arrow{top:412px;color:#fff;font-size:34px;font-weight:700;line-height:1}

/* about */
.about{top:820px;left:0;width:1200px;height:740px}
.about-card{top:200px;width:280px;height:460px;background:#fff;box-shadow:0 4px 18px rgba(0,0,0,.1)}
.about-card .photo{height:200px}
.about-card h3{background:var(--green);color:#fff;font-size:15px;text-align:center;height:30px;line-height:30px}
.about-card p{font-size:12.5px;color:var(--muted);text-align:center;padding:18px 22px;line-height:1.65}

/* is */
.is{top:1560px;left:0;width:1200px;height:500px;background:linear-gradient(#fff,var(--light))}
.is h3{font-size:16px;font-weight:700;white-space:nowrap}
.is ul{list-style:none;font-size:13px;margin-top:18px}
.is li{margin:8px 0}
.ordinary{left:120px;top:210px;width:320px;text-align:right}
.ordinary h3{color:var(--red)}
.ordinary li{color:var(--red)}
.ordinary li::after{content:" ✕"}
.pioneer{left:750px;top:210px;width:340px}
.pioneer h3{color:var(--green)}
.pioneer li{color:var(--green-dark)}
.pioneer li::before{content:"✓ ";color:var(--green)}
.tree{left:465px;top:160px;width:265px;height:310px;border-radius:50% 50% 10px 10px;background:linear-gradient(90deg,#8a8a8a 0%,#b9b9b9 48%,#7fbf4a 52%,#3f9a2f 100%)}

/* services */
.services{top:2060px;left:0;width:1200px;height:640px}
.services .intro{width:860px;margin:18px auto 0;text-align:center;font-size:13.5px;color:var(--muted)}
.svc{top:280px;width:220px;height:280px;background:#fff;box-shadow:0 4px 14px rgba(0,0,0,.12)}
.svc .photo{height:240px}
.svc h4{height:40px;line-height:40px;background:var(--green);color:#fff;text-align:center;font-size:13px}

/* cta */
.cta{top:2700px;left:0;width:1200px;height:220px;background:linear-gradient(90deg,var(--green-dark),var(--green))}
.cta h2{left:160px;top:60px;color:#fff;font-size:28px;font-weight:800;display:flex;align-items:center;gap:14px}
.cta p{left:160px;top:110px;width:700px;color:#e7f4e2;font-size:13.5px}
.cta .btn{left:900px;top:86px}

/* careers */
.careers{top:2940px;left:0;width:1200px;height:680px}
.careers .copy{left:160px;top:180px;width:480px;font-size:13.5px;color:var(--muted)}
.careers .copy p{margin-bottom:14px}
.careers blockquote{color:var(--green);font-style:italic;font-weight:600;margin-bottom:14px}
.careers .heart-photo{left:680px;top:170px;width:360px;height:380px}
.job{left:160px;top:630px;font-family:"Montserrat",sans-serif;font-weight:700;color:var(--green);font-size:17px}
.job-line{left:160px;top:660px;width:880px;height:1px;background:var(--line)}

/* contact */
.contact{top:3620px;left:0;width:1200px;height:440px}
.contact .intro{width:860px;margin:18px auto 0;text-align:center;font-size:13.5px;color:var(--muted)}
.map{top:4060px;left:0;width:1200px;height:220px;background:linear-gradient(135deg,#e9efe6,#dfe7dc 50%,#eef1ea)}
.info{left:160px;top:4320px;width:260px}
.info-item{display:flex;gap:14px;margin-bottom:30px;font-size:12.5px;color:var(--muted)}
.info-item b{display:block;color:var(--ink);font-size:13px}
.info-item svg{flex:none}
.form{left:440px;top:4320px;width:600px}
.field{border:1px solid var(--line);height:38px;font-size:12px;color:#999;padding:10px 14px;margin-bottom:16px}
.row{display:flex;gap:16px}.row .field{flex:1}
.field.tall{height:100px}
.form .btn{float:right}

/* footer */
.footer{top:4630px;left:0;width:1200px;height:350px;background:linear-gradient(#fff 50%,#d9ecc9)}
.footer .brand{color:var(--green-dark)}
.fcol h4{font-size:17px;margin-bottom:16px;color:var(--ink)}
.fcol ul{list-style:none;font-size:13px;color:var(--muted)}
.fcol li{margin-bottom:6px}
.fcol li::before{content:"› ";color:var(--green)}
.social{display:flex;gap:8px}
.social span{width:30px;height:30px;background:var(--green);display:block}
.copyright{top:4980px;left:0;width:1200px;height:80px;background:var(--green-dark);color:#fff;font-size:12px;text-align:center;line-height:80px}
</style>
</head>
<body>

<!-- Hero -->
<div class="abs hero" role="img" aria-label="Photo of an electric delivery van driving on a green tree-lined road"></div>
<div class="abs topbar">
  <span><svg width="12" height="12" viewBox="0 0 24 24"><path fill="#8cc63f" d="M6.6 10.8a15 15 0 0 0 6.6 6.6l2.2-2.2a1 1 0 0 1 1-.25 11 11 0 0 0 3.6.6 1 1 0 0 1 1 1V20a1 1 0 0 1-1 1A17 17 0 0 1 3 4a1 1 0 0 1 1-1h3.5a1 1 0 0 1 1 1c0 1.25.2 2.45.6 3.6a1 1 0 0 1-.25 1z"/></svg>+49 30 555 0142</span>
  <span><svg width="12" height="12" viewBox="0 0 24 24"><path fill="#8cc63f" d="M2 5h20v14H2zm2 2v.5l8 5 8-5V7z"/></svg>info@quillbylogistics.com</span>
</div>
<header class="abs nav">
  <div class="brand"><i></i>Quillby Logistics</div>
  <nav class="menu"><span>HOME</span><span class="active">ABOUT</span><span>SERVICES</span><span>CAREERS</span><span>CONTACT</span></nav>
  <div class="lang"><span></span><span></span></div>
</header>
<div class="abs arrow" style="left:130px">‹</div>
<div class="abs arrow" style="left:1055px">›</div>
<div class="abs hero-content">
  <div class="eyebrow">Welcome to Quillby Logistics</div>
  <h1>QUILLBY LOGISTICS - SUSTAINABLE LAST MILE</h1>
  <p>Quillby Logistics is a pioneer in urban green logistics and provides zero-emissions last mile delivery services with a 100% electric commercial vehicle fleet, fair and sustainable working conditions for its employees and an unparalleled professional and customer-focused mindset.</p>
  <span class="btn"><span class="dot"></span>Get started</span>
</div>

<!-- About -->
<section class="abs about">
  <div class="abs" style="top:100px;width:1200px">
    <div class="eyebrow">Introduction</div>
    <h2 class="section-title">About Us</h2>
    <svg class="heart" viewBox="0 0 24 22"><path fill="#3fa535" d="M12 21 2 11a6 6 0 0 1 10-7 6 6 0 0 1 10 7z"/></svg>
  </div>
  <article class="abs about-card" style="left:152px">
    <div class="photo" role="img" aria-label="Photo of an electric van on a green meadow" style="background:linear-gradient(#bfe0f0,#7cc04a)"></div>
    <h3>Who We Are</h3>
    <p>Quillby Logistics is a pioneer in urban green logistics and provides zero-emission last mile delivery services. We take on urban parcel delivery for our clients with a 100% electric commercial fleet, fair and sustainable working conditions for our employees and a truly professional, customer-focused mindset.</p>
  </article>
  <article class="abs about-card" style="left:460px">
    <div class="photo" role="img" aria-label="Photo of hands holding a young tree" style="background:linear-gradient(#eef3e8,#6aa84f)"></div>
    <h3>Our Mission</h3>
    <p>To satisfy consumers' ever rising demand as e-commerce grows, the CO2 emissions of parcel delivery traffic will increase by 2030. Our mission is to deliver every parcel with zero emissions and leave a greener city behind, so that last mile logistics becomes truly environmentally friendly.</p>
  </article>
  <article class="abs about-card" style="left:768px">
    <div class="photo" role="img" aria-label="Photo of a smiling delivery employee in a green shirt" style="background:linear-gradient(#d6e9c8,#3f9a2f)"></div>
    <h3>Our Values</h3>
    <p>We see ourselves as a professional service company that changes how the delivery industry treats people and the environment – clients, customers and employees alike. We believe that delivering parcels with zero emissions and providing a unique customer experience go hand in hand.</p>
  </article>
</section>

<!-- Quillby Logistics Is -->
<section class="abs is">
  <div class="abs" style="top:60px;width:1200px">
    <div class="eyebrow">Our Difference</div>
    <h2 class="section-title">Quillby Logistics Is:</h2>
    <svg class="heart" viewBox="0 0 24 22"><path fill="#3fa535" d="M12 21 2 11a6 6 0 0 1 10-7 6 6 0 0 1 10 7z"/></svg>
  </div>
  <div class="abs ordinary">
    <h3>An Ordinary Parcel Delivery Firm</h3>
    <ul><li>Polluting our cities</li><li>Always in a rush</li><li>Short-term mindset</li><li>Focusing on profits only</li><li>Not another parcel delivery firm</li></ul>
  </div>
  <div class="abs tree" role="img" aria-label="Illustration of a tree half bare and grey, half green and leafy"></div>
  <div class="abs pioneer">
    <h3>A Pioneering Green Last Mile Firm</h3>
    <ul><li>Delivering parcels emission-free</li><li>Putting customer experience first</li><li>Operating the business sustainably</li><li>Environment, customers and employees</li><li>A professional service company</li></ul>
  </div>
</section>

<!-- Services -->
<section class="abs services">
  <div class="abs" style="top:100px;width:1200px">
    <div class="eyebrow">What we offer</div>
    <h2 class="section-title">Our Services</h2>
    <svg class="heart" viewBox="0 0 24 22"><path fill="#3fa535" d="M12 21 2 11a6 6 0 0 1 10-7 6 6 0 0 1 10 7z"/></svg>
    <p class="intro">Quillby Logistics provides last mile delivery services in urban areas to clients in the logistics and retail space. Our permanent employees are all highly trained and commit to highest professional standards which we continuously review and further develop with them.</p>
  </div>
  <div class="abs svc" style="left:160px"><div class="photo" role="img" aria-label="Photo of electric vans charging" style="background:linear-gradient(#9fcf7a,#2e7d32)"></div><h4>Zero Emission Delivery</h4></div>
  <div class="abs svc" style="left:400px"><div class="photo" role="img" aria-label="Photo of a courier handing over a parcel" style="background:linear-gradient(#c9dfb5,#4e8f3a)"></div><h4>Professional &amp; Friendly</h4></div>
  <div class="abs svc" style="left:640px"><div class="photo" role="img" aria-label="Photo of a delivery driver carrying boxes" style="background:linear-gradient(#d7e8c6,#3a8d2f)"></div><h4>Highly Trained Drivers</h4></div>
  <div class="abs svc" style="left:880px"><div class="photo" role="img" aria-label="Photo of a customer receiving a parcel at the door" style="background:linear-gradient(#e6eee0,#5c9c45)"></div><h4>Best Customer Focus</h4></div>
</section>

<!-- CTA -->
<section class="abs cta">
  <h2 class="abs"><svg width="26" height="24" viewBox="0 0 24 22"><path fill="#fff" d="M12 21 2 11a6 6 0 0 1 10-7 6 6 0 0 1 10 7z"/></svg>GET IN TOUCH WITH QUILLBY LOGISTICS!</h2>
  <p class="abs">If you are looking to learn more about our services, have a question about our approach or would like to join the team, we would be glad to hear from you. Please reach out and we will get back soon.</p>
  <span class="abs btn"><span class="dot"></span>Contact us</span>
</section>

<!-- Careers -->
<section class="abs careers">
  <div class="abs" style="top:90px;width:1200px">
    <div class="eyebrow">Want to join us</div>
    <h2 class="section-title">Careers</h2>
    <svg class="heart" viewBox="0 0 24 22"><path fill="#3fa535" d="M12 21 2 11a6 6 0 0 1 10-7 6 6 0 0 1 10 7z"/></svg>
  </div>
  <div class="abs copy">
    <p>If you join Quillby Logistics, you join a family. We care about one another, care for each other's wellbeing and growth, and celebrate our successes. We strongly believe growth is a process and that every member of the family contributes to the achievement of the company overall.</p>
    <p>At the heart of everything we do at Quillby Logistics is a relentless focus on our mission. That's why we aim to ensure our employees can follow their own passion at the workplace, be it working in a truly collaborative and caring team, putting a smile on a customer's face or making the world a better place.</p>
    <blockquote>"While we are helping our clients grow by delivering their parcels, we are also helping all of our employees grow personally and professionally."</blockquote>
    <p>We care about our employees' happiness and well-being which is why we are providing the additional benefits like fair supplementary health insurance. If you are really excited about joining our Quillby Logistics family, please check out below our open positions.</p>
  </div>
  <svg class="abs heart-photo" viewBox="0 0 360 380" role="img" aria-label="Heart-shaped photo of a smiling driver in a green uniform inside a delivery van">
    <defs><linearGradient id="hg" x1="0" y1="0" x2="1" y2="1"><stop offset="0" stop-color="#cfe3c0"/><stop offset="1" stop-color="#2f8a2b"/></linearGradient></defs>
    <path d="M180 370 20 200C-30 140 10 20 100 20c40 0 65 20 80 50 15-30 40-50 80-50 90 0 130 120 80 180z" fill="url(#hg)"/>
  </svg>
  <div class="abs job">+ Full-time Driver / Parcel Deliverer (M/F/D) for Berlin</div>
  <div class="abs job-line"></div>
</section>

<!-- Contact -->
<section class="abs contact">
  <div class="abs" style="top:200px;width:1200px">
    <div class="eyebrow">Reach out to Quillby Logistics</div>
    <h2 class="section-title">Contact Us</h2>
    <svg class="heart" viewBox="0 0 24 22"><path fill="#3fa535" d="M12 21 2 11a6 6 0 0 1 10-7 6 6 0 0 1 10 7z"/></svg>
    <p class="intro">Whether you have a question about our services, our approach, our jobs or just want to get in touch to chat how green logistics can make the planet a little bit better, our team is ready to answer your questions and enquiries.</p>
  </div>
</section>
<div class="abs map" role="img" aria-label="Street map of Berlin showing the company location"></div>

<div class="abs info">
  <div class="info-item"><svg width="18" height="20" viewBox="0 0 24 24"><path fill="#3fa535" d="M12 2a7 7 0 0 0-7 7c0 5 7 13 7 13s7-8 7-13a7 7 0 0 0-7-7zm0 9.5A2.5 2.5 0 1 1 12 6.5a2.5 2.5 0 0 1 0 5z"/></svg><div><b>Location:</b>Linden Straße 12, 10115 Berlin</div></div>
  <div class="info-item"><svg width="18" height="20" viewBox="0 0 24 24"><path fill="#3fa535" d="M2 5h20v14H2zm2 2v.5l8 5 8-5V7z"/></svg><div><b>Email Address:</b>info@quillbylogistics.com</div></div>
  <div class="info-item"><svg width="18" height="20" viewBox="0 0 24 24"><path fill="#3fa535" d="M6.6 10.8a15 15 0 0 0 6.6 6.6l2.2-2.2a1 1 0 0 1 1-.25 11 11 0 0 0 3.6.6 1 1 0 0 1 1 1V20a1 1 0 0 1-1 1A17 17 0 0 1 3 4a1 1 0 0 1 1-1h3.5a1 1 0 0 1 1 1c0 1.25.2 2.45.6 3.6a1 1 0 0 1-.25 1z"/></svg><div><b>Phone Number:</b>+49 30 555 0142</div></div>
</div>
<form class="abs form">
  <div class="row"><div class="field">Full Name*</div><div class="field">Email Address*</div></div>
  <div class="field">Subject*</div>
  <div class="field tall">Type your message here</div>
  <span class="btn"><span class="dot"></span>Send message</span>
</form>

<!-- Footer -->
<footer class="abs footer" role="contentinfo">
  <div class="abs" style="left:160px;top:50px;width:260px">
    <div class="brand" style="font-size:16px"><i></i>Quillby Logistics</div>
    <p style="font-size:12.5px;color:var(--muted);margin-top:14px">We want to make the planet a better place by creating more environmentally friendly urban logistics, fair and sustainable working conditions, and an unparalleled customer experience.</p>
  </div>
  <div class="abs fcol" style="left:460px;top:50px"><h4>Quick Links</h4><ul><li>Home</li><li>About</li><li>Services</li><li>Careers</li><li>Contact</li></ul></div>
  <div class="abs fcol" style="left:680px;top:50px"><h4>Information</h4><ul><li>Privacy Policy</li><li>Legal Notice</li></ul></div>
  <div class="abs fcol" style="left:920px;top:50px"><h4>Find Us At</h4><div class="social"><span></span><span></span><span></span></div></div>
</footer>
<div class="abs copyright">Copyright © 2020 Quillby Logistics - All Rights Reserved</div>

</body>
</html>
```